Powerpoint Presentation design template

I am looking for a PPT presentation that show class and professionalism and in the same colour them as the logo. It should be simple, but yet classy and pro. The business is an oil and gas exploration and exploitation business. The business has nothing to do with solar panel and other renewable energies, so please no solar panel or wind farms in the background. It would be more oil rigs and LNG plant in the background of some slide templates...

oil and gas exploration and exploitation

```html
<!DOCTYPE html>
<html lang="en">
<head>
<meta charset="utf-8">
<title>Azobe Energy – Presentation Template</title>
<link href="https://fonts.googleapis.com/css2?family=Montserrat:wght@400;500;600&display=swap" rel="stylesheet">
<style>
:root{
  --blue:#1a9fd0;
  --teal:#14a39a;
  --green:#3fae49;
  --ink:#1b1b1b;
  --dark:#171818;
  --paper:#f4f4f4;
  --band:#e5ebeb;
  --rule:#1aa59c;
  --url:#2bb8b0;
}
*{margin:0;padding:0;box-sizing:border-box}
html,body{width:684px;height:1200px;overflow:hidden;background:#fff}
body{font-family:'Montserrat',sans-serif;color:var(--ink);position:relative}
.brand{position:absolute;display:flex;align-items:center;gap:8px;color:var(--blue);font-weight:600;white-space:nowrap}
.brand .dot{border-radius:50%;background:var(--blue);flex:none}
.sheet-brand{left:0;width:684px;top:36px;justify-content:center;font-size:26px}
.sheet-brand .dot{width:40px;height:40px}
.sheet-title{position:absolute;top:101px;width:684px;text-align:center;color:var(--blue);font-size:16px;font-weight:500;letter-spacing:.3px}
.label{position:absolute;font-size:9px;font-weight:600;transform:translateX(-50%)}
.slide{position:absolute;width:285px;height:205px;background:var(--paper);overflow:hidden}
.slide .head-dot{position:absolute;left:11px;top:4px;width:17px;height:17px;border-radius:50%;background:var(--teal)}
.slide .head-name{position:absolute;right:5px;top:8px;font-size:7.5px;color:var(--blue);font-weight:500}
.slide .head-rule{position:absolute;left:0;right:0;top:24px;height:1px;background:var(--rule)}
.footer{position:absolute;left:0;bottom:0;width:285px;height:20px;background:var(--dark);border-top:2px solid var(--teal)}
.footer .url{position:absolute;right:22px;top:5px;font-size:7px;color:var(--url);font-weight:500;letter-spacing:.2px}
.photo-bg{position:absolute;inset:0;background:linear-gradient(180deg,#eef1f3 0%,#f3ece9 45%,#e9eef1 100%)}
.cover-brand{left:0;width:285px;justify-content:center;font-size:14px}
.cover-brand .dot{width:22px;height:22px}
.cover-kicker{position:absolute;top:78px;width:285px;text-align:center;font-size:8.5px;font-weight:500}
.cover-title{position:absolute;top:93px;width:285px;text-align:center;font-size:12px;line-height:18px;color:var(--blue);font-weight:500}
.stmt{position:absolute;left:42px;width:232px;font-size:6.4px;line-height:11px}
.stmt b{font-weight:600}
.icon{position:absolute;left:9px;width:20px;height:20px}
.photo{position:absolute}
.body-text{position:absolute;font-size:6.6px;line-height:11.3px}
.slide-h{position:absolute;color:var(--blue);font-weight:500}
.band{position:absolute;left:0;right:0;top:114px;bottom:0;background:var(--band)}
.bullet{position:absolute;width:7px;height:7px;border-radius:50%;background:var(--teal)}
.hse-h{position:absolute;left:25px;font-size:6.8px;color:var(--teal);font-weight:500}
.hse-d{position:absolute;left:25px;width:250px;font-size:6.5px;line-height:11px}
.faint{position:absolute;left:25px;top:152px;font-size:12px;font-weight:600;color:#d3e7ee}
.col-h{position:absolute;font-size:7.2px}
.col{position:absolute;list-style:none;font-size:5.7px;line-height:8px;font-family:Arial,sans-serif}
.col li{position:relative;padding-left:8px;margin-bottom:4px}
.col li::before{content:"›";position:absolute;left:0;top:-1px;font-size:7px;font-weight:600}
.adv{position:absolute;left:25px;width:252px;font-size:6.6px;line-height:11.3px}
.adv b{font-weight:600}
.thanks{position:absolute;top:96px;width:285px;text-align:center;font-size:19px;font-weight:500}
.end-brand{left:390px;top:1026px;font-size:28px}
.end-brand .dot{width:50px;height:50px}
</style>
</head>
<body>

<div class="brand sheet-brand"><span class="dot"></span>Azobe Energy</div>
<div class="sheet-title">PPT DESIGN</div>

<!-- Slide 1: cover -->
<section class="slide" style="left:49px;top:149px">
  <div class="photo-bg" role="img" aria-label="Faded photograph of oil pumpjacks at an oil field"></div>
  <div class="brand cover-brand" style="top:16px"><span class="dot"></span>Azobe Energy</div>
  <div class="cover-kicker">Title of The Presentation</div>
  <div class="cover-title">Oil and Gas Exploration and<br>Exploitation Business</div>
  <div class="footer"><span class="url">www.azobeenergy.com</span></div>
</section>
<div class="label" style="left:182px;top:363px">Slide 1</div>

<!-- Slide 2: mission -->
<section class="slide" style="left:346px;top:149px">
  <span class="head-dot"></span><span class="head-name">Azobe Energy</span><span class="head-rule"></span>
  <svg class="icon" style="top:37px" viewBox="0 0 20 20" fill="none" stroke="var(--blue)" stroke-width="1.6">
    <circle cx="9" cy="11" r="7.5"/><circle cx="9" cy="11" r="4"/><circle cx="9" cy="11" r="1" fill="var(--blue)"/>
    <path d="M9 11 L18 3" stroke="var(--green)"/></svg>
  <div class="stmt" style="top:38px"><b>Mission Statement:</b> To responsibly explore, extract, and deliver energy solutions for a sustainable future.</div>
  <svg class="icon" style="top:66px" viewBox="0 0 20 20" fill="none" stroke="var(--blue)" stroke-width="1.6">
    <circle cx="12" cy="8" r="5.5"/><circle cx="12" cy="8" r="2"/><path d="M8 12 L2 18"/></svg>
  <div class="stmt" style="top:67px"><b>Vision Statement:</b> To be a global leader in oil and gas exploration and production, driving energy innovations.</div>
  <svg class="icon" style="top:96px" viewBox="0 0 20 20" fill="none" stroke="var(--blue)" stroke-width="1.5">
    <path d="M10 9 C6 6 7 2 10 4 C13 2 14 6 10 9Z" fill="var(--green)" stroke="var(--green)"/>
    <path d="M1 11 L5 17 L9 17 L9 13 M19 11 L15 17 L11 17 L11 13"/></svg>
  <div class="stmt" style="top:100px"><b>Core Values:</b> Safety, Sustainability, Innovation, Integrity, Excellence</div>
  <div class="photo" style="left:11px;top:125px;width:62px;height:47px;background:linear-gradient(180deg,#b8c4cc,#8e7a5c 60%,#6d5a42)" role="img" aria-label="Photograph of a drilling rig crew on site"></div>
  <div class="body-text" style="left:79px;top:125px;width:196px">Lorem ipsum dolor sit amet, consectetuer adipiscing elit, sed diam nonummy nibh euismod tincidunt ut laoreet dolore magna aliquam.</div>
  <div class="footer"><span class="url">www.azobeenergy.com</span></div>
</section>
<div class="label" style="left:480px;top:363px">Slide 2</div>

<!-- Slide 3: regulatory -->
<section class="slide" style="left:49px;top:401px">
  <div class="band"></div>
  <span class="head-dot"></span><span class="head-name">Azobe Energy</span><span class="head-rule"></span>
  <div class="slide-h" style="left:12px;top:35px;font-size:9.3px;line-height:14px;width:115px">Regulatory Changes In Emissions And Environmental Impact</div>
  <div class="body-text" style="left:12px;top:81px;width:112px">Lorem ipsum dolor sit amtetuer adipiscing elit, sed diam nummy nibh euismod tincidunt.</div>
  <div class="body-text" style="left:12px;top:117px;width:115px">Lorem ipsum dolor loresit amet, consectetuer adipiscing elit, sed diam nonummy nibh euismod tincidunt ut laoreet.</div>
  <div class="photo" style="left:131px;top:36px;width:146px;height:122px;background:linear-gradient(180deg,#f7c25a 0%,#f3a63b 55%,#8a5a2e 80%,#3d2a1c 100%)" role="img" aria-label="Photograph of an oil pumpjack at sunset"></div>
  <div class="footer"><span class="url">www.azobeenergy.com</span></div>
</section>
<div class="label" style="left:177px;top:617px">Slide 3</div>

<!-- Slide 4: HSE -->
<section class="slide" style="left:346px;top:401px">
  <span class="head-dot"></span><span class="head-name">Azobe Energy</span><span class="head-rule"></span>
  <div class="slide-h" style="left:0;width:285px;text-align:center;top:34px;font-size:11px">Health, Safety &amp; Environmental Responsibility</div>
  <span class="bullet" style="left:11px;top:65px"></span>
  <div class="hse-h" style="top:63px">Health and Safety Programs</div>
  <div class="hse-d" style="top:73px">Strict safety protocols to ensure the well-being of workers &amp; communities.</div>
  <span class="bullet" style="left:11px;top:93px"></span>
  <div class="hse-h" style="top:91px">Environmental Impact Assessment (EIA)</div>
  <div class="hse-d" style="top:100px">Evaluating potential environmental effects before beginning operations.</div>
  <span class="bullet" style="left:11px;top:120px"></span>
  <div class="hse-h" style="top:118px">Sustainability Measures</div>
  <div class="hse-d" style="top:127px">Carbon Emission Reduction Initiatives, Waste Management Systems &amp; Spill Response Plans</div>
  <div class="faint">Azobe Energy</div>
  <div class="footer"><span class="url">www.azobeenergy.com</span></div>
</section>
<div class="label" style="left:475px;top:617px">Slide 4</div>

<!-- Slide: exploitation -->
<section class="slide" style="left:50px;top:678px">
  <span class="head-dot"></span><span class="head-name">Azobe Energy</span><span class="head-rule"></span>
  <div class="slide-h" style="left:0;width:285px;text-align:center;top:34px;font-size:11px">Exploitation and Production</div>
  <div class="body-text" style="left:0;width:285px;text-align:center;top:51px">Lorem ipsum dolor sit amet, consectetuer adipiscing elit, sed diam.</div>
  <div class="col-h" style="left:19px;top:69px">Drilling Technologies</div>
  <ul class="col" style="left:19px;top:86px;width:110px">
    <li>Offshore (Platform and Subsea)</li>
    <li>Onshore (Land Drilling)</li>
    <li>Advanced drilling techniques (horizontal, fracking)</li>
    <li>Lorem ipsum dolor sit amet</li>
    <li>Lorem ipsum dolor sit amet doir ectetuer adipiscing elit, sed.</li>
  </ul>
  <div class="col-h" style="left:146px;top:69px">Production Stages</div>
  <ul class="col" style="left:146px;top:86px;width:130px">
    <li>Well Completion: Installing equipment for oil/gas extraction.</li>
    <li>Extraction: Pumping oil/gas to the surface.</li>
    <li>Transportation: Pipeline or tanker systems to move resources to refineries.</li>
    <li>Lorem ipsum dolor sit amet doir ectetuer lore adipiscing elit, sed.</li>
  </ul>
  <div class="footer"><span class="url">www.azobeenergy.com</span></div>
</section>
<div class="label" style="left:185px;top:891px">Slide 4</div>

<!-- Slide 5: competitive advantage -->
<section class="slide" style="left:354px;top:678px">
  <span class="head-dot"></span><span class="head-name">Azobe Energy</span><span class="head-rule"></span>
  <div class="photo" style="left:149px;top:35px;width:122px;height:68px;background:radial-gradient(ellipse at 50% 40%,#b8b8b8,#d9d9d9 60%,var(--paper) 80%)" role="img" aria-label="Grey world map"></div>
  <div style="position:absolute;left:12px;top:36px;font-size:11px;line-height:16px;font-weight:500">Lorem Ipsum Dolor<br>Sit Amet onsectetuer<br>Adipiscing.</div>
  <div class="slide-h" style="left:12px;top:88px;font-size:11px">Competitive Advantage</div>
  <span class="bullet" style="left:12px;top:113px"></span>
  <div class="adv" style="top:109px"><b>Proven Track Record:</b> Highlight successful projects or reserves discovered.</div>
  <span class="bullet" style="left:12px;top:128px"></span>
  <div class="adv" style="top:124px"><b>Technological Expertise:</b> Specialized in innovative drilling, exploration, and data analysis techniques.</div>
  <span class="bullet" style="left:12px;top:151px"></span>
  <div class="adv" style="top:147px"><b>Strong Partnerships:</b> Collaborations with other major industry players, governments, and financial institutions.</div>
  <div class="footer"><span class="url">www.azobeenergy.com</span></div>
</section>
<div class="label" style="left:483px;top:891px">Slide 5</div>

<!-- Slide 6: thank you -->
<section class="slide" style="left:50px;top:938px">
  <div class="photo-bg" role="img" aria-label="Faded photograph of oil pumpjacks at an oil field"></div>
  <div class="brand cover-brand" style="top:58px"><span class="dot"></span>Azobe Energy</div>
  <div class="thanks">Thank You</div>
  <div class="footer"><span class="url">www.azobeenergy.com</span></div>
</section>
<div class="label" style="left:183px;top:1150px">Slide 6</div>

<div class="brand end-brand"><span class="dot"></span>Azobe Energy</div>

</body>
</html>
```